Business Card Design

We need a business card designed which uses our logo and looks really good. The company is called LumaPivot482. We help e-commerce companies reduce cart abandonment by rescuing the sale through our innovative technology.

Our corporate colors are red, black and white.

I have attached our AI file for the logo as well.
Updates

Additional information for the business card:

Name: Derek Malloy
Title: President/CTO
Phone: 1-855-LUMA-482
Website: www.lumapivot482.com
Email: derek@lumapivot482.com

Tag line: Turning Browsers Into Buyers

Industry/Entity Type

E-Commerce

```html
<!DOCTYPE html>
<html lang="en">
<head>
<meta charset="utf-8">
<title>LumaPivot482 Business Card</title>
<link rel="stylesheet" href="https://fonts.googleapis.com/css2?family=Arimo:wght@400;700&family=Open+Sans:wght@400;600&display=swap">
<style>
  :root {
    --backdrop: #3b3b3d;
    --card: #f2f2f2;
    --band: #4a4a4c;
    --ink: #1c1c1c;
    --accent: #d21f26;
    --tagline: #e6e6e6;
  }
  * { box-sizing: border-box; margin: 0; padding: 0; }
  html, body {
    width: 1200px; height: 780px; overflow: hidden;
    background: var(--backdrop);
  }
  .stage {
    width: 1200px; height: 780px;
    display: flex; align-items: center; justify-content: center;
  }
  .card {
    position: relative;
    width: 900px; height: 514px;
    background: var(--card);
    font-family: "Arimo", Arial, sans-serif;
    color: var(--ink);
    box-shadow: 0 18px 40px rgba(0,0,0,0.35);
    overflow: hidden;
  }
  .card-bands { position: absolute; inset: 0; }
  .brand {
    position: absolute; left: 60px; top: 168px;
    display: flex; align-items: center; gap: 12px;
    font-size: 40px; font-weight: 400; letter-spacing: 1px;
    color: var(--ink);
  }
  .brand-square { width: 22px; height: 22px; background: var(--accent); }
  .contact {
    position: absolute; left: 400px; top: 148px;
  }
  .contact-head { font-size: 30px; margin-bottom: 10px; }
  .contact-name { font-weight: 700; }
  .contact-title { font-weight: 400; margin-left: 10px; }
  .contact-list { list-style: none; }
  .contact-item {
    display: flex; align-items: center; gap: 14px;
    font-size: 27px; line-height: 40px;
  }
  .contact-icon { width: 22px; height: 22px; flex: none; }
  .tagline {
    position: absolute; left: 40px; bottom: 14px;
    font-family: "Open Sans", Arial, sans-serif;
    font-size: 28px; font-weight: 400;
    letter-spacing: 6px; text-transform: uppercase;
    color: var(--tagline);
    white-space: nowrap;
  }
</style>
</head>
<body>
<main class="stage">
  <article class="card">
    <svg class="card-bands" viewBox="0 0 900 514" width="900" height="514" aria-hidden="true">
      <polygon points="0,0 900,0 900,36 720,36 670,100 620,36 0,36" fill="var(--band)"/>
      <polygon points="0,448 540,448 600,390 660,448 900,448 900,514 0,514" fill="var(--band)"/>
    </svg>

    <div class="brand">
      <span class="brand-name">LumaPivot482</span>
      <span class="brand-square"></span>
    </div>

    <section class="contact">
      <h1 class="contact-head">
        <span class="contact-name">Derek Malloy</span><span class="contact-title">President / CTO</span>
      </h1>
      <ul class="contact-list">
        <li class="contact-item">
          <svg class="contact-icon" viewBox="0 0 24 24" aria-hidden="true"><path fill="var(--accent)" d="M6.6 10.8a15.1 15.1 0 0 0 6.6 6.6l2.2-2.2a1 1 0 0 1 1-.25 11.4 11.4 0 0 0 3.6.57 1 1 0 0 1 1 1V20a1 1 0 0 1-1 1A17 17 0 0 1 3 4a1 1 0 0 1 1-1h3.5a1 1 0 0 1 1 1c0 1.25.2 2.45.57 3.57a1 1 0 0 1-.25 1z"/></svg>
          <span>1-855-LUMA-482</span>
        </li>
        <li class="contact-item">
          <svg class="contact-icon" viewBox="0 0 24 24" aria-hidden="true"><rect x="2" y="5" width="20" height="14" rx="2" fill="var(--accent)"/><path d="M3 6l9 7 9-7" fill="none" stroke="var(--card)" stroke-width="1.8"/></svg>
          <span>derek@lumapivot482.com</span>
        </li>
        <li class="contact-item">
          <svg class="contact-icon" viewBox="0 0 24 24" aria-hidden="true"><circle cx="12" cy="12" r="10" fill="var(--accent)"/><path d="M2 12h20M12 2c3 3 3 17 0 20M12 2c-3 3-3 17 0 20" fill="none" stroke="var(--card)" stroke-width="1.4"/></svg>
          <span>www.lumapivot482.com</span>
        </li>
      </ul>
    </section>

    <p class="tagline">Turning Browsers Into Buyers</p>
  </article>
</main>
</body>
</html>
```